Kestavon Values/Culture for employees

Take our cultures list and create an on brand graphic that can be used for various media, ie. posters, screen savers etc. mykestavon.com
We're a medium sized company who installs permanent christmas lights primarily for homeowners. however we will do it for businesses as well. This graphic is going to be for our employees to help remind them the cultures and values we stand for to provide the best experience and products. Since Christmas lights are such an important part of our country's culture we want to make sure the internal culture of the company reflects that.

Target Market(s)

People who want to imrpove their home with permanent chrismas lights and never install them again

Requirements
Must have
• Proper styling with our brand colors and font (gotham)

Style guide is attached.

```html
<!DOCTYPE html>
<html lang="en">
<head>
<meta charset="utf-8">
<title>Kestavon — Our Cultural Beliefs</title>
<link rel="stylesheet" href="https://fonts.googleapis.com/css2?family=Montserrat:wght@300;500;600;800&display=swap">
<style>
  :root {
    --blue: #2771f7;
    --teal: #35c99a;
    --green: #6cc21c;
    --yellow: #f5c20f;
    --orange: #fa8a12;
    --red: #f4230f;
    --pink: #f23cb7;
    --purple: #9a10d9;
    --ink: #111111;
    --paper: #ffffff;
  }
  * { margin: 0; padding: 0; box-sizing: border-box; }
  html, body { width: 1200px; height: 925px; overflow: hidden; background: var(--paper); }
  .poster {
    position: relative;
    width: 1200px;
    height: 925px;
    background: var(--paper);
    font-family: "Montserrat", "Helvetica Neue", Arial, sans-serif;
    color: var(--ink);
    overflow: hidden;
  }
  .title-block {
    position: absolute;
    left: 0; top: 77px;
    width: 431px; height: 221px;
    background: var(--blue);
    color: #fff;
    padding: 18px 0 0 65px;
    line-height: 0.98;
  }
  .title-block .lead { display: block; font-weight: 300; font-size: 54px; letter-spacing: 1px; }
  .title-block .main { display: block; font-weight: 800; font-size: 60px; letter-spacing: 1px; margin-top: 6px; }
  .art { position: absolute; left: 0; top: 0; width: 1200px; height: 925px; }
  .brand {
    position: absolute;
    left: 49px; top: 790px;
    display: flex; align-items: center; gap: 14px;
    font-weight: 600; font-size: 34px; letter-spacing: 9px;
    color: var(--ink);
  }
  .brand .dot { width: 16px; height: 16px; border-radius: 50%; background: var(--blue); }
  .value { position: absolute; }
  .value h2 {
    font-weight: 800; font-size: 31px; line-height: 0.98;
    letter-spacing: 0.5px; text-transform: uppercase;
    padding-bottom: 6px;
    position: relative;
  }
  .value h2::after, .value p::after {
    content: ""; position: absolute; left: 0; bottom: 0;
    width: 120px; height: 2px;
    background: linear-gradient(90deg, var(--c), transparent);
  }
  .value p {
    font-weight: 600; font-size: 19px; line-height: 22px;
    padding: 6px 0 6px; position: relative;
  }
  .customer { left: 742px; top: 41px; --c: var(--green); }
  .own      { left: 940px; top: 224px; --c: var(--yellow); }
  .simplify { left: 940px; top: 457px; --c: var(--orange); }
  .trust    { left: 742px; top: 651px; --c: var(--red); }
  .seize    { left: 521px; top: 651px; --c: var(--pink); }
  .now      { left: 324px; top: 449px; --c: var(--purple); }
  .value h2 { color: var(--c); }
  .own h2 { color: #f2a90a; }
</style>
</head>
<body>
<main class="poster">
  <svg class="art" viewBox="0 0 1200 925" aria-hidden="true">
    <defs>
      <linearGradient id="ray" x1="0" y1="0" x2="1" y2="0">
        <stop offset="0" stop-color="#999" stop-opacity="0"/>
        <stop offset="0.5" stop-color="#888" stop-opacity="0.7"/>
        <stop offset="1" stop-color="#999" stop-opacity="0"/>
      </linearGradient>
    </defs>

    <!-- accent stripe -->
    <polygon class="stripe" points="85,345 88,345 476,925 460,925" fill="var(--teal)"/>

    <!-- radiating guide lines -->
    <g class="rays" stroke-width="1.5">
      <line x1="714" y1="180" x2="714" y2="690" stroke="url(#ray)"/>
      <line x1="468" y1="428" x2="960" y2="428" stroke="url(#ray)"/>
      <line x1="540" y1="602" x2="890" y2="252" stroke="url(#ray)"/>
      <line x1="540" y1="254" x2="890" y2="604" stroke="url(#ray)"/>
    </g>

    <!-- value wheel -->
    <g class="wheel">
      <path d="M714,238 A190,190 0 0 1 848.4,293.6 L787.5,354.5 A104,104 0 0 0 714,324 Z" fill="var(--green)"/>
      <path d="M848.4,293.6 A190,190 0 0 1 904,428 L818,428 A104,104 0 0 0 787.5,354.5 Z" fill="var(--yellow)"/>
      <path d="M904,428 A190,190 0 0 1 848.4,562.4 L787.5,501.5 A104,104 0 0 0 818,428 Z" fill="var(--orange)"/>
      <path d="M848.4,562.4 A190,190 0 0 1 714,618 L714,532 A104,104 0 0 0 787.5,501.5 Z" fill="var(--red)"/>
      <path d="M714,618 A190,190 0 0 1 579.6,562.4 L640.5,501.5 A104,104 0 0 0 714,532 Z" fill="var(--pink)"/>
      <path d="M579.6,562.4 A190,190 0 0 1 524,428 L610,428 A104,104 0 0 0 640.5,501.5 Z" fill="var(--purple)"/>
      <!-- outer rim shading -->
      <g fill="#000" opacity="0.16">
        <path d="M714,238 A190,190 0 0 1 904,428 L886,428 A172,172 0 0 0 714,256 Z"/>
        <path d="M904,428 A190,190 0 0 1 524,428 L542,428 A172,172 0 0 0 886,428 Z"/>
      </g>
    </g>

    <!-- wheel icons -->
    <g class="icons" fill="none" stroke="#fff" stroke-width="2" stroke-linecap="round" stroke-linejoin="round">
      <g transform="translate(770,292)">
        <circle cx="-6" cy="-14" r="10"/>
        <path d="M-26,16 C-26,0 -16,-2 -6,-2 C2,-2 8,0 12,4"/>
        <path d="M-26,16 L4,16"/>
        <circle cx="16" cy="14" r="9"/>
        <path d="M11,14 L15,18 L21,10"/>
      </g>
      <g transform="translate(850,372)">
        <circle cx="-8" cy="-18" r="8"/>
        <rect x="-22" y="2" width="9" height="18"/>
        <rect x="-8" y="-6" width="9" height="26"/>
        <rect x="6" y="-14" width="9" height="34"/>
        <rect x="20" y="-22" width="9" height="42"/>
        <path d="M-26,20 L30,20"/>
      </g>
      <g transform="translate(850,484)">
        <path d="M-16,24 L-16,12 C-26,4 -26,-16 -10,-22 C4,-28 20,-18 18,-4 L22,4 L16,6 L16,14 L6,14 L6,24"/>
        <circle cx="0" cy="-4" r="6"/>
        <circle cx="0" cy="-4" r="11" stroke-dasharray="4 3"/>
      </g>
      <g transform="translate(770,564)">
        <path d="M-28,-6 L-14,-18 L-2,-12 L8,-18 L28,-6"/>
        <path d="M-22,0 L-8,12 C-4,16 0,16 4,12 L20,-2"/>
        <path d="M-2,-12 L-12,-2 C-10,2 -4,2 0,-2 L6,-6"/>
      </g>
      <g transform="translate(658,564)">
        <path d="M-14,-20 L14,-20 L12,0 C10,8 4,10 0,10 C-4,10 -10,8 -12,0 Z"/>
        <path d="M-14,-14 C-24,-14 -22,0 -12,0"/>
        <path d="M14,-14 C24,-14 22,0 12,0"/>
        <path d="M0,10 L0,18 M-10,18 L10,18 L10,24 L-10,24 Z"/>
      </g>
      <g transform="translate(578,484)">
        <circle cx="4" cy="4" r="20"/>
        <path d="M4,-8 L4,4 L12,10"/>
        <path d="M-2,-22 L10,-22 M4,-22 L4,-16"/>
        <path d="M-26,0 L-20,0 M-28,8 L-20,8 M-24,16 L-18,16"/>
      </g>
    </g>
  </svg>

  <header class="title-block">
    <h1><span class="lead">OUR</span><span class="main">CULTURAL<br>BELIEFS</span></h1>
  </header>

  <section class="value customer">
    <h2>Customer<br>First</h2>
    <p>I strive to meet our<br>customer’s needs and<br>deliver exceptional<br>experiences.</p>
  </section>
  <section class="value own">
    <h2>Own It</h2>
    <p>I demonstrate<br>commitment by<br>showing up “all<br>in,” all the time,<br>even when it<br>requires sacrifice.</p>
  </section>
  <section class="value simplify">
    <h2>Simplify</h2>
    <p>I eliminate<br>complexity and<br>solve problems<br>for sustainable<br>results.</p>
  </section>
  <section class="value trust">
    <h2>Build<br>Trust</h2>
    <p>I trust people to do<br>their best, let them<br>perform and then coach<br>them to perform at<br>even higher levels.</p>
  </section>
  <section class="value seize">
    <h2>Seize<br>The Day</h2>
    <p>I am a big part of<br>something big.<br>What I do today<br>will help us win<br>together!</p>
  </section>
  <section class="value now">
    <h2>Do It Now</h2>
    <p>I work above the<br>line, continue to<br>ask “What else<br>can I do to deliver<br>results?” and<br>refuse to blame<br>others.</p>
  </section>

  <div class="brand"><span class="dot"></span>KESTAVON</div>
</main>
</body>
</html>
```